The name of the company is Harbor Turns buying foreclosed homes and remodeling

A sleek classy card. It’s a home remodel and house flip company. Something mostly black with dark gray and red in color . Something with two f”s as a logo on front as shown in pictures. Kind of just let you guys run with it . I left a few pictures that should help
You guys get an idea of what I thought was good also left all the information for back of the card

Target Market(s)

Home remodel consumers

Industry/Entity Type

Construction Company

Contact Information for Business Card

All details are on photo

Font styles to use
Decorative

Colors

Designer to choose colors to be used in the design.

Requirements
Must have
• Name of company on front. Harbor Turns
Nice to have
• Up to you guys I trust you
Should not have
• Not sure

```html
<!DOCTYPE html>
<html lang="en">
<head>
<meta charset="utf-8">
<title>Harbor Turns – Business Card</title>
<link href="https://fonts.googleapis.com/css2?family=Fira+Sans+Condensed:wght@300;400;500&display=swap" rel="stylesheet">
<style>
  :root {
    --page: #ffffff;
    --front-red: #a33649;
    --front-mark: #b9606f;
    --back-gray: #636365;
    --back-mark: #3c3c3e;
    --ink-light: #f4eef0;
    --ink-white: #ffffff;
  }
  * { margin: 0; padding: 0; box-sizing: border-box; }
  html, body {
    width: 927px;
    height: 1200px;
    overflow: hidden;
    background: var(--page);
    font-family: "Fira Sans Condensed", "Arial Narrow", sans-serif;
  }
  .sheet { position: relative; width: 927px; height: 1200px; }

  .card { position: absolute; overflow: hidden; }

  /* Front */
  .card-front {
    left: 266px; top: 301px; width: 389px; height: 221px;
    background: var(--front-red);
  }
  .front-mark {
    position: absolute; left: 425px; top: 376px;
    width: 76px; height: 76px; border-radius: 50%;
    background: var(--front-mark); opacity: 0.55;
  }
  .front-rule {
    position: absolute; left: 174px; top: 150px;
    width: 215px; height: 1px; background: var(--front-mark);
  }
  .front-name {
    position: absolute; left: 216px; top: 160px;
    font-size: 19px; font-weight: 400; color: var(--ink-light);
    letter-spacing: 0.1px;
  }

  /* Back */
  .card-back {
    left: 266px; top: 612px; width: 386px; height: 222px;
    background: var(--back-gray);
  }
  .back-mark {
    position: absolute; left: 8px; top: 211px;
    transform-origin: left top; transform: rotate(-90deg);
    font-size: 30px; font-weight: 500; color: var(--back-mark);
    white-space: nowrap; letter-spacing: 1px;
  }
  .back-rule {
    position: absolute; left: 0; top: 65px;
    width: 208px; height: 2px; background: var(--back-mark);
  }
  .owner {
    position: absolute; left: 66px; top: 38px;
    font-size: 17px; font-weight: 300; color: var(--ink-white);
  }
  .contact-list {
    position: absolute; left: 66px; top: 74px;
    list-style: none; font-size: 15px; font-weight: 300;
    line-height: 21px; color: var(--ink-white);
  }
  .services {
    position: absolute; left: 66px; top: 185px;
    display: flex; gap: 9px;
    font-size: 12px; font-weight: 500; color: var(--ink-white);
    white-space: nowrap;
  }
</style>
</head>
<body>
<main class="sheet">
  <section class="card card-front" aria-label="Card front">
    <div class="front-mark" style="left:159px;top:75px;"></div>
    <div class="front-rule"></div>
    <p class="front-name">Harbor Turns</p>
  </section>

  <section class="card card-back" aria-label="Card back">
    <p class="back-mark">Harbor Turns</p>
    <div class="back-rule"></div>
    <h1 class="owner">Dominic Ashworth, Jr.</h1>
    <ul class="contact-list">
      <li>Dashworthjr@mailbox.com</li>
      <li>Harbor_Turns</li>
      <li>harborturns.com</li>
      <li>555.203.4817</li>
    </ul>
    <p class="services">
      <span>General Contractor</span>
      <span>Home Remodel</span>
      <span>Concrete Alternatives</span>
    </p>
  </section>
</main>
</body>
</html>
```